Fresh look for Client Documents

We have a new software system and it now generates word document reports. We need these tidied up and consistently branded with a stylish corporate theme. We also need to add a "powered by Brimquell" theme to them as the reports are generated by business that use the software so the documents do not exactly 'belong' to their brand. On all of them we need to have the powred by Brimquell PLUS provision for a businesses own logo.
All the documents are generated in Word

```html
<!DOCTYPE html>
<html lang="en">
<head>
<meta charset="utf-8">
<title>Brimquell Client Documents</title>
<link href="https://fonts.googleapis.com/css2?family=Carlito:ital,wght@0,400;0,700;1,400&display=swap" rel="stylesheet">
<style>
:root{
  --stage:#b1b1b1;
  --paper:#ffffff;
  --ink:#1f1f1f;
  --navy:#2b3175;
  --blue:#3d8fd1;
  --slot-line:#b9c2d3;
  --slot-fill:#f2f5fa;
  --hint-fill:#e9eef6;
  --hint-ink:#3a4a6a;
  --note:#d83a3a;
  --row:#d7e0f0;
  --rowtext:#3a5a9c;
  --field:#d8d8d8;
}
*{box-sizing:border-box;margin:0;padding:0}
html,body{width:1200px;height:1029px;overflow:hidden;background:var(--stage)}
body{font-family:"Carlito",Calibri,Arial,sans-serif;color:var(--ink)}
.stage{width:2072px;height:1776px;transform:scale(0.5792);transform-origin:0 0;position:relative;background:var(--stage)}
.page{position:absolute;background:var(--paper);overflow:hidden}
.portrait{width:621px;height:879px}
.landscape{width:877px;height:620px}
.abs{position:absolute;white-space:nowrap}
.logo-slot{position:absolute;width:112px;height:74px;border:1.5px dashed var(--slot-line);background:var(--slot-fill);border-radius:3px}
.footer{position:absolute;left:0;width:100%;height:22px}
.footer svg{position:absolute;left:0;top:0}
.footer-label{position:absolute;top:2px;font-size:12px;color:#fff}
.footer-name{position:absolute;top:-1px;font-size:19px;font-weight:700;color:var(--navy)}
.t11{font-size:11px;line-height:14px}
.hint{background:var(--hint-fill);color:var(--hint-ink);padding:0 3px;border-radius:2px}
.box{display:inline-block;width:9px;height:9px;vertical-align:-1px;margin-left:1px}
.h-title{font-size:23px;font-weight:400}
.work-table{position:absolute;left:59px;top:346px;width:511px;border-collapse:collapse;font-size:11px}
.work-table td{border:1px solid #333;padding:0 5px;vertical-align:top;height:14px}
.qr-list{position:absolute;left:59px;top:599px;width:227px;font-size:13.6px;list-style:none}
.qr-list li{border-bottom:1px solid #e6e6e6;line-height:15.5px;padding-top:0.5px}
.form-grid{position:absolute;left:62px;top:416px;width:470px;height:128px}
.f-label{position:absolute;font-size:5px;font-weight:700}
.f-label b{color:var(--note)}
.f-box{position:absolute;width:110px;height:16px;border:1px solid var(--field);border-radius:2px;font-size:5px;color:#666;padding:5px 5px 0}
.activity{position:absolute;left:45px;top:152px;width:777px;font-size:11px}
.act-head{position:relative;height:16px;color:#555;font-style:italic;border-bottom:1px solid var(--rowtext)}
.act-row{position:relative;height:16px;color:var(--rowtext)}
.act-row.shade::before{content:"";position:absolute;left:81px;right:0;top:0;height:16px;background:var(--row)}
.act-row span,.act-head span{position:absolute;top:1px}
.act-note{height:16px;color:var(--rowtext);font-style:italic;padding-left:5px}
.act-gap{height:16px;position:relative}
.act-gap::before{content:"";position:absolute;left:81px;right:0;top:0;height:16px;background:var(--row)}
.inspect{position:absolute;left:59px;top:118px;width:763px;border-collapse:collapse;font-size:11px}
.inspect td{border:1px solid #333;padding:1px 5px;vertical-align:top;line-height:13px}
.tick{text-align:center}
</style>
</head>
<body>
<svg width="0" height="0" style="position:absolute">
  <defs>
    <symbol id="checked" viewBox="0 0 10 10"><rect x="0.5" y="0.5" width="9" height="9" fill="none" stroke="#222" stroke-width="1"/><path d="M2.3 5.2 L4.2 7.2 L7.8 2.6" fill="none" stroke="#222" stroke-width="1.1"/></symbol>
    <symbol id="unchecked" viewBox="0 0 10 10"><rect x="0.5" y="0.5" width="9" height="9" fill="none" stroke="#222" stroke-width="1"/></symbol>
  </defs>
</svg>
<div class="stage">

  <!-- Contractor work order -->
  <section class="page portrait" style="left:395px;top:108px">
    <div class="logo-slot" style="left:43px;top:18px" role="img" aria-label="Business logo placeholder"></div>
    <div class="abs t11" style="left:59px;top:119px">Management Group: Harbourline Realty<br>Strata Manager: Dana Mercer</div>
    <div class="abs t11" style="left:59px;top:161px">Building details:<br>Peninsula<br>27 Marrow Lane Kingston ACT<br>Approximate Build Date 2016&nbsp; Heritage Listed? No</div>
    <div class="abs t11" style="left:59px;top:217px">No. of Commercial Lots&nbsp; 2</div>
    <div class="abs t11" style="left:209px;top:217px">Retail<svg class="box"><use href="#checked"/></svg></div>
    <div class="abs t11" style="left:272px;top:217px">Commercial/Office</div>
    <div class="abs t11" style="left:397px;top:217px">Industrial</div>
    <div class="abs t11" style="left:59px;top:245px">Storeys 3<br>Pool 1<br>Gym 1</div>
    <div class="abs t11" style="left:134px;top:245px">Basement 2<br>Spa 0<br>Tennis Court 1</div>
    <div class="abs t11" style="left:209px;top:245px">Lifts 4<br>Sauna 0<br>Playground 0</div>
    <div class="abs t11" style="left:322px;top:245px">Escalator 0<br>Steam Room 0<br>BBQ 3</div>
    <h1 class="abs h-title" style="left:59px;top:317px">Contractor Work Order</h1>
    <table class="work-table">
      <tr><td style="width:155px">Area</td><td>Superstructure</td></tr>
      <tr><td>Asset</td><td>Building Membrane</td></tr>
      <tr><td style="height:169px">Strata Manager Comments</td><td></td></tr>
    </table>
    <p class="abs t11" style="left:59px;top:558px;white-space:normal;width:500px">QR Codes have been installed at the following locations in this building. It is a requirement that all service technicians check in on arrival.</p>
    <ul class="qr-list">
      <li>Fire Indicator Panel - Building One</li>
      <li>Pedestrian Access Door Two - Main Level Carpark</li>
      <li>Pedestrian Access Door One - Main Level Carpark</li>
      <li>Main Level Carpark - Notice Board Two</li>
      <li>Main Level Carpark - Notice Board One</li>
      <li>Basement Notice Board</li>
      <li>Elevator - Building Two</li>
      <li>Elevator - Building One</li>
      <li>Front Door - Building Two</li>
      <li>Front Door - Building One</li>
    </ul>
    <div class="footer" style="top:833px">
      <svg width="621" height="22"><polygon points="0,0 440,0 431,22 0,22" fill="var(--blue)"/><polygon points="570,0 621,0 621,22 560,22" fill="var(--navy)"/></svg>
      <span class="footer-label" style="left:355px">powered by</span>
      <span class="footer-name" style="left:446px">BRIMQUELL</span>
    </div>
  </section>

  <!-- Insurance quotation brief -->
  <section class="page portrait" style="left:1056px;top:108px">
    <div class="logo-slot" style="left:48px;top:22px" role="img" aria-label="Business logo placeholder"></div>
    <h1 class="abs" style="left:59px;top:120px;font-size:28px;font-weight:400">Insurance Quotation Brief</h1>
    <div class="abs t11" style="left:59px;top:236px">Date <span class="hint">(today’s date)</span></div>
    <div class="abs t11" style="left:59px;top:260px">Strata Management Group <span class="hint">(Name)</span></div>
    <div class="abs t11" style="left:59px;top:283px">Strata Manager <span class="hint">(Name – Email)</span></div>
    <div class="abs t11" style="left:59px;top:307px">Please find information relative to the insurance renewal application for:</div>
    <div class="abs t11" style="left:59px;top:330px"><span class="hint">Building Name &amp; Address</span></div>
    <p class="abs t11" style="left:59px;top:377px;white-space:normal;width:500px;line-height:15px;font-weight:700;color:var(--navy)">Building information</p>
    <div class="form-grid">
      <span class="f-label" style="left:0;top:2px">Units Plan Number</span>
      <span class="f-label" style="left:117px;top:2px">Building Name</span>
      <span class="f-label" style="left:234px;top:2px">Block<b>*</b></span>
      <span class="f-label" style="left:351px;top:2px">Section<b>*</b></span>
      <div class="f-box" style="left:0;top:11px;color:#aaa">Unit Plan Number</div>
      <div class="f-box" style="left:117px;top:11px">Orion Test Building</div>
      <div class="f-box" style="left:234px;top:11px">1</div>
      <div class="f-box" style="left:351px;top:11px">test</div>
      <span class="f-label" style="left:0;top:33px">Units<b>*</b></span>
      <span class="f-label" style="left:117px;top:33px">Street No.<b>*</b></span>
      <span class="f-label" style="left:234px;top:33px">Street Name<b>*</b></span>
      <span class="f-label" style="left:351px;top:33px">Suburb<b>*</b></span>
      <div class="f-box" style="left:0;top:42px">10</div>
      <div class="f-box" style="left:117px;top:42px">234</div>
      <div class="f-box" style="left:234px;top:42px">test street</div>
      <div class="f-box" style="left:351px;top:42px">Acton</div>
      <span class="f-label" style="left:0;top:64px">State<b>*</b></span>
      <span class="f-label" style="left:117px;top:64px">Postcode<b>*</b></span>
      <span class="f-label" style="left:234px;top:64px">Build Date</span>
      <span class="f-label" style="left:351px;top:64px">Builder</span>
      <div class="f-box" style="left:0;top:73px">ACT</div>
      <div class="f-box" style="left:117px;top:73px">2601</div>
      <div class="f-box" style="left:234px;top:73px;color:#aaa">Build Date</div>
      <div class="f-box" style="left:351px;top:73px;color:#aaa">Builder</div>
      <span class="f-label" style="left:0;top:95px">Insurance Company<b>*</b></span>
      <span class="f-label" style="left:117px;top:95px">Certificate Expiry Date<b>*</b></span>
      <span class="f-label" style="left:240px;top:98px;font-size:4px">Building Class</span>
      <div class="f-box" style="left:0;top:104px">test insurance</div>
      <div class="f-box" style="left:117px;top:104px">14-Sep-2022</div>
      <div class="f-box" style="left:240px;top:104px;width:86px;height:12px;padding-top:3px;font-size:4px">Class A</div>
    </div>
    <div class="abs t11" style="left:59px;top:557px;font-weight:700">Insurance claims history for past 24 months:</div>
    <div class="abs t11" style="left:59px;top:580px">Claims made?&nbsp; Yes<svg class="box"><use href="#checked"/></svg>&nbsp;&nbsp;&nbsp;&nbsp;&nbsp;&nbsp; No<svg class="box"><use href="#unchecked"/></svg></div>
    <div class="abs t11" style="left:59px;top:604px">Details: <span class="hint">free text area</span></div>
    <div class="abs t11" style="left:59px;top:651px;font-weight:700">Routine, Safety &amp; Compliance Inspections Register:</div>
    <div class="abs t11" style="left:59px;top:674px"><span class="hint">Upcoming periodic inspections</span></div>
    <div class="footer" style="top:837px">
      <svg width="621" height="22"><polygon points="0,0 445,0 436,22 0,22" fill="var(--blue)"/><polygon points="573,0 621,0 621,22 563,22" fill="var(--navy)"/></svg>
      <span class="footer-label" style="left:359px">powered by</span>
      <span class="footer-name" style="left:451px">BRIMQUELL</span>
    </div>
  </section>

  <!-- Building activity summary -->
  <section class="page landscape" style="left:136px;top:1046px">
    <div class="logo-slot" style="left:21px;top:16px" role="img" aria-label="Business logo placeholder"></div>
    <div class="abs t11" style="left:59px;top:104px;font-weight:700">Building Activity Summary for past 24 months:</div>
    <div class="activity">
      <div class="act-head"><span style="left:5px">Date</span><span style="left:86px">Area</span><span style="left:234px">Item</span><span style="left:382px">Comment Category</span><span style="left:562px">Company</span><span style="left:725px">Cost</span></div>
      <div class="act-row shade"><span style="left:5px">19/5/2022</span><span style="left:86px">Basement</span><span style="left:234px">Garage Door Motors</span><span style="left:382px">Defect</span><span style="left:562px">Kelso Industries</span><span style="left:725px">$4500</span></div>
      <div class="act-note">Vsghgsvvhgvahgvgvdshgavsagsdhavhsvdsgvgsavgvagvgavavsvagvhasavagsavgvshs</div>
      <div class="act-row shade"><span style="left:5px">19/5/2022</span><span style="left:86px">Basement</span><span style="left:234px">Garage Door Motors</span><span style="left:382px">Defect</span><span style="left:562px">Kelso Industries</span><span style="left:725px">$4500</span></div>
      <div class="act-note">Vsghgsvvhgvahgvgvdshgavsagsdhavhsvdsgvgsavgvagvgavavsvagvhasavagsavgvshs</div>
      <div class="act-row shade"><span style="left:5px">19/5/2022</span><span style="left:86px">Basement</span><span style="left:234px">Garage Door Motors</span><span style="left:382px">Defect</span><span style="left:562px">Kelso Industries</span><span style="left:725px">$4500</span></div>
      <div class="act-note">Vsghgsvvhgvahgvgvdshgavsagsdhavhsvdsgvgsavgvagvgavavsvagvhasavagsavgvshs</div>
      <div class="act-row shade"><span style="left:5px">19/5/2022</span><span style="left:86px">Basement</span><span style="left:234px">Garage Door Motors</span><span style="left:382px">Defect</span><span style="left:562px">Kelso Industries</span><span style="left:725px">$4500</span></div>
      <div class="act-note">Vsghgsvvhgvahgvgvdshgavsagsdhavhsvdsgvgsavgvagvgavavsvagvhasavagsavgvshs</div>
      <div class="act-gap"></div>
      <div class="act-row"><span style="left:5px">19/5/2022</span><span style="left:86px">Basement</span><span style="left:234px">Garage Door Motors</span><span style="left:382px">Defect</span><span style="left:562px">Kelso Industries</span><span style="left:725px">$4500</span></div>
      <div class="act-note">Vsghgsvvhgvahgvgvdshgavsagsdhavhsvdsgvgsavgvagvgavavsvagvhasavagsavgvshs</div>
      <div class="act-row"><span style="left:5px">19/5/2022</span><span style="left:86px">Basement</span><span style="left:234px">Garage Door Motors</span><span style="left:382px">Defect</span><span style="left:562px">Kelso Industries</span><span style="left:725px">$4500</span></div>
      <div class="act-note">Vsghgsvvhgvahgvgvdshgavsagsdhavhsvdsgvgsavgvagvgavavsvagvhasavagsavgvshs</div>
      <div class="act-row shade" style="margin-top:16px"><span style="left:5px">19/5/2022</span><span style="left:86px">Basement</span><span style="left:234px">Garage Door Motors</span><span style="left:382px">Defect</span><span style="left:562px">Kelso Industries</span><span style="left:725px">$4500</span></div>
      <div class="act-note">Vsghgsvvhgvahgvgvdshgavsagsdhavhsvdsgvgsavgvagvgavavsvagvhasavagsavgvshs</div>
      <div class="act-row shade"><span style="left:5px">19/5/2022</span><span style="left:86px">Basement</span><span style="left:234px">Garage Door Motors</span><span style="left:382px">Defect</span><span style="left:562px">Kelso Industries</span><span style="left:725px">$4500</span></div>
      <div class="act-note">Vsghgsvvhgvahgvgvdshgavsagsdhavhsvdsgvgsavgvagvgavavsvagvhasavagsavgvshs</div>
      <div class="act-gap"></div>
      <div class="act-row"><span style="left:5px">19/5/2022</span><span style="left:86px">Basement</span><span style="left:234px">Garage Door Motors</span><span style="left:382px">Defect</span><span style="left:562px">Kelso Industries</span><span style="left:725px">$4500</span></div>
      <div class="act-note">Vsghgsvvhgvahgvgvdshgavsagsdhavhsvdsgvgsavgvagvgavavsvagvhasavagsavgvshs</div>
      <div class="act-row"><span style="left:5px">19/5/2022</span><span style="left:86px">Basement</span><span style="left:234px">Garage Door Motors</span><span style="left:382px">Defect</span><span style="left:562px">Kelso Industries</span><span style="left:725px">$4500</span></div>
      <div class="act-note">Vsghgsvvhgvahgvgvdshgavsagsdhavhsvdsgvgsavgvagvgavavsvagvhasavagsavgvshs</div>
    </div>
    <div class="footer" style="top:572px">
      <svg width="877" height="22"><polygon points="0,0 700,0 691,22 0,22" fill="var(--blue)"/><polygon points="823,0 877,0 877,22 813,22" fill="var(--navy)"/></svg>
      <span class="footer-label" style="left:612px">powered by</span>
      <span class="footer-name" style="left:703px">BRIMQUELL</span>
    </div>
  </section>

  <!-- Inspection checklist -->
  <section class="page landscape" style="left:1057px;top:1046px">
    <div class="logo-slot" style="left:23px;top:16px" role="img" aria-label="Business logo placeholder"></div>
    <table class="inspect">
      <tr><td colspan="7" style="height:43px">Building Name<br>Building Address<br>Management Group</td></tr>
      <tr style="height:29px"><td style="width:140px"></td><td style="width:128px"></td><td style="width:61px">Defect Observed?</td><td style="width:49px">Minor</td><td style="width:58px">Moderate</td><td style="width:46px">Major</td><td>Comments</td></tr>
      <tr><td>Area</td><td>Item</td><td class="tick"><svg class="box"><use href="#checked"/></svg></td><td class="tick"><svg class="box"><use href="#checked"/></svg></td><td class="tick"><svg class="box"><use href="#checked"/></svg></td><td class="tick"><svg class="box"><use href="#checked"/></svg></td><td></td></tr>
      <tr style="height:29px"><td>Basement &amp; Internal Car Accommodation</td><td>Kerbs and line marking (repaint)</td><td></td><td></td><td></td><td></td><td></td></tr>
      <tr style="height:29px"><td></td><td>Gas detection Unit</td><td></td><td></td><td></td><td></td><td></td></tr>
      <tr style="height:29px"><td></td><td>Roller shutter doors</td><td></td><td></td><td></td><td></td><td></td></tr>
      <tr style="height:29px"><td></td><td>Motion Sensors</td><td></td><td></td><td></td><td></td><td></td></tr>
      <tr style="height:29px"><td></td><td>Driveway</td><td></td><td></td><td></td><td></td><td></td></tr>
      <tr style="height:29px"><td>Bathrooms &amp; Toilets</td><td>Joinery</td><td></td><td></td><td></td><td></td><td></td></tr>
      <tr style="height:29px"><td></td><td>Toilet</td><td></td><td></td><td></td><td></td><td></td></tr>
      <tr style="height:29px"><td>Elevator</td><td></td><td></td><td></td><td></td><td></td><td></td></tr>
    </table>
    <div class="footer" style="top:572px">
      <svg width="877" height="22"><polygon points="0,0 700,0 691,22 0,22" fill="var(--blue)"/><polygon points="823,0 877,0 877,22 813,22" fill="var(--navy)"/></svg>
      <span class="footer-label" style="left:612px">powered by</span>
      <span class="footer-name" style="left:703px">BRIMQUELL</span>
    </div>
  </section>

</div>
</body>
</html>
```